ARC VOLLEY Business Card Project

I'd like to request a business card design for the new company I've launched.
The name of the company is "ARC VOLLEY" an indoor unmanned tennis practice facility.
We would like to see designs that use our brand identity color in the logo I've attached.
We hope to get the design with modern, luxurious and elegant tone and manner.
We hope the logo should not be too big.

Business card must have elements as below:
- Logo (One of the logos I've attached)
- Name (In Korean Text) : 박 서 윤
- Title (In Korean Text) : 대표
- Phone Number : 010-8472-3916
- Email Address : seoyun.park@arcvolley-example.co.kr
- Website : www.arcvolley-example.co.kr
- Instagram : arcvolley
- Address (In Korean text) : 경기도 용인시 수지구 풍덕천로 456 미래타워 5층 501호, 502호

Target Market(s)

Tennis amateurs in 20 to 40s

Industry/Entity Type

Sports, Hobby

Contact Information for Business Card

- Logo (One of the logos I've attached) - Name (In Korean Text) : 박 서 윤 - Title (In Korean Text) : 대표 - Phone Number : 010-8472-3916 - Email Address : seoyun.park@arcvolley-example.co.kr - Website : www.arcvolley-example.co.kr - Instagram : arcvolley - Address (In Korean text) : 경기도 용인시 수지구 풍덕천로 456 미래타워 5층 501호, 502호

Font styles to use
Sans Serif

Requirements
Must have
• Double sided
Nice to have
• Logo with intaglio or relief embossing
Should not have
• Logo should not be too big.

```html
<!DOCTYPE html>
<html lang="ko">
<head>
<meta charset="utf-8">
<title>ARC VOLLEY Business Card</title>
<link rel="stylesheet" href="https://fonts.googleapis.com/css2?family=Montserrat:wght@400;500&family=Noto+Sans+KR:wght@400;500;700&display=swap">
<style>
  :root {
    --backdrop: #d7d7d7;
    --card-green: #264d31;
    --foil-gold: #c9a13c;
    --card-shadow: rgba(0, 0, 0, 0.22);
  }
  * { box-sizing: border-box; margin: 0; padding: 0; }
  html, body {
    width: 1200px;
    height: 846px;
    overflow: hidden;
    background: var(--backdrop);
  }
  .sheet {
    width: 1200px;
    height: 846px;
    display: flex;
    align-items: center;
    justify-content: center;
    gap: 40px;
  }
  .card {
    position: relative;
    width: 540px;
    height: 300px;
    background: var(--card-green);
    color: var(--foil-gold);
    box-shadow: 0 10px 24px var(--card-shadow);
  }
  .brand-name {
    font-family: "Montserrat", "Helvetica Neue", Arial, sans-serif;
    font-weight: 500;
    letter-spacing: 0.08em;
    color: var(--foil-gold);
    white-space: nowrap;
  }

  /* Front side */
  .card-front .brand-name {
    position: absolute;
    left: 44px;
    top: 48px;
    font-size: 30px;
  }
  .person {
    position: absolute;
    left: 44px;
    top: 140px;
    font-family: "Noto Sans KR", sans-serif;
    font-weight: 700;
  }
  .person-name { font-size: 21px; letter-spacing: 0.05em; line-height: 1.3; white-space: nowrap; }
  .person-title { font-size: 17px; font-weight: 500; line-height: 1.4; }
  .divider {
    position: absolute;
    left: 142px;
    top: 138px;
    width: 1px;
    height: 122px;
    background: var(--foil-gold);
    opacity: 0.8;
  }
  .contacts {
    position: absolute;
    left: 158px;
    top: 136px;
    width: 362px;
    list-style: none;
    font-family: "Montserrat", "Noto Sans KR", sans-serif;
    font-size: 11.5px;
  }
  .contacts li {
    display: flex;
    align-items: flex-start;
    gap: 8px;
    min-height: 23px;
    line-height: 16px;
  }
  .contacts .address { font-family: "Noto Sans KR", sans-serif; font-size: 11px; }
  .contact-icon { width: 13px; height: 13px; margin-top: 1.5px; flex: none; fill: var(--foil-gold); }
  .contact-icon.outline { fill: none; stroke: var(--foil-gold); stroke-width: 2; }

  /* Back side */
  .card-back {
    display: flex;
    align-items: center;
    justify-content: center;
    gap: 18px;
  }
  .brand-dot {
    width: 50px;
    height: 50px;
    border-radius: 50%;
    background: var(--foil-gold);
  }
  .card-back .brand-name { font-size: 38px; }
</style>
</head>
<body>
  <main class="sheet">
    <section class="card card-front" aria-label="Business card front">
      <div class="brand-name">ARC VOLLEY</div>
      <div class="person">
        <p class="person-name">박 서 윤</p>
        <p class="person-title">대표</p>
      </div>
      <div class="divider"></div>
      <ul class="contacts">
        <li>
          <svg class="contact-icon" viewBox="0 0 24 24" aria-hidden="true"><path d="M6.6 10.8a15.1 15.1 0 0 0 6.6 6.6l2.2-2.2a1 1 0 0 1 1-.25 11.4 11.4 0 0 0 3.6.57 1 1 0 0 1 1 1V20a1 1 0 0 1-1 1A17 17 0 0 1 3 4a1 1 0 0 1 1-1h3.5a1 1 0 0 1 1 1c0 1.25.2 2.45.57 3.6a1 1 0 0 1-.25 1z"/></svg>
          <span>010-8472-3916</span>
        </li>
        <li>
          <svg class="contact-icon" viewBox="0 0 24 24" aria-hidden="true"><path d="M2 5h20v14H2z M4 7v.4l8 5.2 8-5.2V7z" fill-rule="evenodd"/></svg>
          <span>seoyun.park@arcvolley-example.co.kr</span>
        </li>
        <li>
          <svg class="contact-icon outline" viewBox="0 0 24 24" aria-hidden="true"><circle cx="12" cy="12" r="9"/><path d="M3 12h18M12 3c3 3 3 15 0 18M12 3c-3 3-3 15 0 18"/></svg>
          <span>www.arcvolley-example.co.kr</span>
        </li>
        <li>
          <svg class="contact-icon outline" viewBox="0 0 24 24" aria-hidden="true"><circle cx="12" cy="12" r="8"/></svg>
          <span>arcvolley</span>
        </li>
        <li class="address">
          <svg class="contact-icon" viewBox="0 0 24 24" aria-hidden="true"><path d="M12 2a7 7 0 0 0-7 7c0 5 7 13 7 13s7-8 7-13a7 7 0 0 0-7-7zm0 9.5A2.5 2.5 0 1 1 12 6.5a2.5 2.5 0 0 1 0 5z"/></svg>
          <span>경기도 용인시 수지구 풍덕천로 456 미래타워 5층 501호, 502호</span>
        </li>
      </ul>
    </section>

    <section class="card card-back" aria-label="Business card back">
      <span class="brand-dot"></span>
      <span class="brand-name">ARC VOLLEY</span>
    </section>
  </main>
</body>
</html>
```